Website Design & Development For a New Start Up

We require a bespoke website design and development.
Requirements:
We want something similar to www.pelmorabank.com... not exact as this is copywrite infringement... but we want you to get a feel for the site and design accordingly. We will leave the creativity to you.
All logos, detailed content and description will be given upon seeing the designs and your eye for creativity. here are our requirements.
1. Upto 20 internal pages. Clean simple design that will be discussed with developer.
2. Account Opening sections - Very detailed client sign up. 4 types of client to sign up (Bespoke account information required for each client)
3. Client Login Area. Client Authentication tools.
4. Admin and Client area - where documents and information will be stored.
5. Live API currency feeds into front end.
6. Document security and Website security is very important as we will be holding client information
7. We want the website to be RESPONSIVE on ALL smart Phones and Tablyx etc. Website MUST work on all browsers regardless of age.
8. We would like ALL coding to be done in CLEAN HTML5 and it must work effortlessly for clients when they touch any button etc.
We want a designer and developer that has the eye for intricate aesthetic design and technical ability to execute functional perfectly and make the user experience effortless.
We look forward to seeing your designs and working with you.
Regards
Quarlen Team
Reason: We are still getting designs and we have yet to get it perfected so we are waiting for more submissions. Thanks
Financial Money Transaction
Security

```html
<!DOCTYPE html>
<html lang="en">
<head>
<meta charset="utf-8">
<title>Quarlen — The best way to move money</title>
<link href="https://fonts.googleapis.com/css2?family=Ubuntu:wght@300;400;500&family=Marcellus+SC&display=swap" rel="stylesheet">
<style>
:root{
  --brand:#1a8fc4;
  --brand-band:#1b97c8;
  --tab-dark:#1a5877;
  --ink:#444;
  --muted:#888;
  --green-dark:#4a9c1e;
  --footer:#050505;
  --footer-text:#bbb;
  --grey-btn:#ddd;
}
*{box-sizing:border-box;margin:0;padding:0}
html,body{width:800px;height:1200px;overflow:hidden}
body{position:relative;font-family:"Ubuntu",sans-serif;color:var(--ink);background:#fff}

/* header */
.site-header{position:absolute;left:0;top:0;width:800px;height:60px;background:#fff}
.brand{position:absolute;left:58px;top:15px;font-size:25px;font-weight:400;color:var(--brand);letter-spacing:1px}
.nav-link{position:absolute;top:23px;font-size:11px;color:var(--brand)}
.btn-signup{position:absolute;left:597px;top:18px;width:70px;height:24px;background:var(--grey-btn);border-radius:2px;font-size:11px;color:#333;display:flex;align-items:center;justify-content:center;gap:5px}
.btn-login{position:absolute;left:684px;top:18px;width:57px;height:24px;background:var(--brand);border-radius:2px;font-size:11px;color:#fff;display:flex;align-items:center;justify-content:center;gap:5px}

/* hero */
.hero-photo{position:absolute;left:0;top:60px;width:800px;height:353px;background:linear-gradient(110deg,#d9d6d2 0%,#ece9e6 35%,#c7b9a8 55%,#6d93c8 70%,#e8e5e0 100%)}
.quote-panel{position:absolute;left:74px;top:186px;width:652px;height:104px;background:rgba(70,70,70,.78)}
.field{position:absolute;top:32px;height:29px;width:120px;background:#fff;font-size:11px;color:#222;padding-left:12px;display:flex;align-items:center}
.select{position:absolute;top:32px;height:29px;width:65px;background:#2a9fd6;color:#fff;font-size:12px;padding-left:10px;display:flex;align-items:center}
.select svg{position:absolute;right:10px;top:11px}
.btn-start{position:absolute;left:449px;top:32px;width:185px;height:29px;background:linear-gradient(#68c43a,var(--green-dark));color:#fff;font-size:13px;font-weight:500;letter-spacing:1px;display:flex;align-items:center;justify-content:center}
.saving{position:absolute;left:0;top:80px;width:652px;text-align:center;font-size:11px;color:#fff;font-weight:300}
.saving .why{color:#8ad33f;margin-left:18px}
.dot{position:absolute;top:387px;width:7px;height:7px;border-radius:50%;background:#fff}

/* intro */
.intro-title{position:absolute;left:0;top:442px;width:800px;text-align:center;font-family:"Marcellus SC",serif;font-weight:400;font-size:19px;color:#333;letter-spacing:1.5px}
.intro-text{position:absolute;left:86px;top:473px;width:628px;text-align:center;font-size:8.4px;line-height:14.5px;color:var(--muted)}
.feature{position:absolute;top:532px;width:200px;text-align:center}
.feature-ring{margin:0 auto;width:98px;height:98px;border-radius:50%;background:#eee;display:flex;align-items:center;justify-content:center}
.feature-icon{width:86px;height:86px;border-radius:50%;background:var(--brand);display:flex;align-items:center;justify-content:center}
.feature h3{margin-top:20px;font-size:16.5px;font-weight:400;color:var(--brand)}
.feature p{margin-top:9px;font-size:7.6px;line-height:13px;color:var(--muted)}

/* info band */
.info-band{position:absolute;left:0;top:726px;width:800px;height:229px;background:var(--brand-band)}
.tab{position:absolute;left:59px;width:200px;height:31px;background:var(--tab-dark);clip-path:polygon(0 0,86% 0,100% 50%,86% 100%,0 100%);color:#fff;font-size:14px;display:flex;align-items:center;padding-left:47px}
.tab svg{position:absolute;left:15px;top:7px}
.tab.active{background:#fff;color:var(--brand)}
.video-frame{position:absolute;left:287px;top:29px;width:226px;height:172px;background:#fff;padding:4px}
.video-still{width:100%;height:100%;background:linear-gradient(90deg,#eef3f6 0%,#dfe8ee 55%,#c9c4bd 80%,#b8b0a6 100%);position:relative}
.play{position:absolute;left:95px;top:66px;width:34px;height:34px;border-radius:50%;background:rgba(30,60,80,.55);border:2px solid #fff}
.play::after{content:"";position:absolute;left:12px;top:8px;border-left:11px solid #fff;border-top:7px solid transparent;border-bottom:7px solid transparent}
.info-copy{position:absolute;left:542px;top:27px;width:200px;font-size:7.8px;line-height:15.8px;color:#fff}
.info-copy p+p{margin-top:15.8px}
.know-more{position:absolute;left:542px;top:190px;font-size:11px;color:#1d4e66;display:flex;align-items:center;gap:10px}

/* partners */
.partners{position:absolute;left:0;top:955px;width:800px;height:97px;background:#fff}
.partner{position:absolute;top:40px;font-size:11px;color:#666;display:flex;align-items:center;gap:5px}
.partner i{display:inline-block;width:12px;height:12px;background:#999;border-radius:50%}

/* footer */
.site-footer{position:absolute;left:0;top:1052px;width:800px;height:148px;background:var(--footer);color:var(--footer-text)}
.footer-brand{position:absolute;left:58px;top:12px;font-size:23px;color:var(--brand);letter-spacing:1px}
.legal{position:absolute;left:59px;top:61px;font-size:7px;line-height:14px;color:#ddd}
.social{position:absolute;top:96px;width:25px;height:25px;border-radius:50%;background:#e0e0e0;border:2px solid #888}
.footer-heading{position:absolute;top:24px;font-size:13.5px;font-weight:400;color:#fff}
.news-input{position:absolute;left:237px;top:52px;width:123px;height:22px;background:#eee;border:1px solid #999;font-size:6.5px;color:#555;padding-left:10px;display:flex;align-items:center}
.news-btn{position:absolute;left:236px;top:85px;width:58px;height:19px;background:var(--brand);border:1px solid #6cc0e6;color:#fff;font-size:9px;display:flex;align-items:center;justify-content:center}
.news-item{position:absolute;left:426px;width:170px;font-size:7.3px;line-height:11.5px;color:#999}
.news-item .date,.news-item .meta{color:var(--brand)}
.find-us{position:absolute;left:637px;top:50px;width:150px;font-size:7.3px;line-height:11.5px;color:#999}
.find-us a{color:var(--brand);text-decoration:none}
</style>
</head>
<body>

<header class="site-header">
  <div class="brand">Quarlen</div>
  <span class="nav-link" style="left:470px">How It Works</span>
  <span class="nav-link" style="left:556px">Help</span>
  <div class="btn-signup">
    <svg width="10" height="10" viewBox="0 0 10 10"><rect x="0.7" y="1.5" width="7" height="7.5" fill="none" stroke="#333" stroke-width="1.2"/><path d="M4 6 9 1" stroke="#333" stroke-width="1.4"/></svg>Sign up
  </div>
  <div class="btn-login">
    <svg width="9" height="10" viewBox="0 0 9 10"><circle cx="4.5" cy="2.8" r="2.5" fill="#fff"/><path d="M0 10c0-3.5 2-5 4.5-5S9 6.5 9 10z" fill="#fff"/></svg>Login
  </div>
</header>

<section>
  <div class="hero-photo" role="img" aria-label="Photo of a smiling woman relaxing on a sofa with a laptop"></div>
  <form class="quote-panel">
    <div class="field" style="left:18px">Send Money</div>
    <div class="select" style="left:138px">USD<svg width="8" height="7" viewBox="0 0 8 7"><path d="M1 0 4 3 7 0M1 3.5 4 6.5 7 3.5" fill="none" stroke="#fff" stroke-width="1.2"/></svg></div>
    <div class="field" style="left:234px">Receive Money</div>
    <div class="select" style="left:354px">INR<svg width="8" height="7" viewBox="0 0 8 7"><path d="M1 0 4 3 7 0M1 3.5 4 6.5 7 3.5" fill="none" stroke="#fff" stroke-width="1.2"/></svg></div>
    <div class="btn-start">Get Started</div>
    <div class="saving">You'll save P0.00 vs your bank <span class="why">+Why Us?</span></div>
  </form>
  <span class="dot" style="left:385px"></span>
  <span class="dot" style="left:397px"></span>
  <span class="dot" style="left:408px;width:9px;height:9px;top:386px;background:#fff;box-shadow:inset 0 0 0 2px #fff,inset 0 0 0 4px #333"></span>
</section>

<section>
  <h1 class="intro-title">The Best Way to Move Money</h1>
  <p class="intro-text">Neque porro quisquam est, qui dolorem ipsum quia dolor sit amet, consectetur, adipisci velit, sed quia non numquam eius modi tempora incidunt ut labore et dolore magnam aliquam quaerat voluptatem. Ut enim ad minima veniam, quis nostrum exercitationem ullam corporis suscipit laboriosam.Neque porro magnam aliquam quaerat voluptatem. Ut enim ad minima veniam, quis nostrum exercitationem ullam corporis suscipit laboriosam</p>

  <div class="feature" style="left:72px">
    <div class="feature-ring"><div class="feature-icon">
      <svg width="50" height="50" viewBox="0 0 50 50"><circle cx="25" cy="25" r="22" fill="none" stroke="#fff" stroke-width="2.5"/><path d="M25 7v4M13 12l3 3M37 12l-3 3M9 25h4M37 25h4" stroke="#fff" stroke-width="2"/><path d="M30 16 23 32" stroke="#fff" stroke-width="2.5"/><circle cx="22" cy="33" r="3" fill="none" stroke="#fff" stroke-width="2"/></svg>
    </div></div>
    <h3>High Speed</h3>
    <p>Sed ut perspiciatis unde omnis iste natus error sit<br>totam rem aperiam, eaque ipsa quae ab illo.</p>
  </div>
  <div class="feature" style="left:300px">
    <div class="feature-ring"><div class="feature-icon">
      <svg width="42" height="42" viewBox="0 0 42 42"><rect x="2" y="19" width="8" height="19" fill="#fff"/><path d="M13 19 21 9c1-3 2-6 4-6 3 0 4 3 3 7l-2 6h11c3 0 4 3 2 5 2 1 2 4 0 5 1 2 0 4-2 5 1 2-1 4-3 4H13z" fill="#fff"/></svg>
    </div></div>
    <h3>Faster &amp; Simple</h3>
    <p>Sed ut perspiciatis unde omnis iste natus error sit<br>totam rem aperiam, eaque ipsa quae ab illo.</p>
  </div>
  <div class="feature" style="left:528px">
    <div class="feature-ring"><div class="feature-icon">
      <svg width="42" height="38" viewBox="0 0 42 38"><circle cx="9" cy="10" r="5" fill="#fff"/><circle cx="33" cy="10" r="5" fill="#fff"/><circle cx="21" cy="9" r="7" fill="#fff"/><path d="M1 26c0-6 3-9 8-9s8 3 8 9zM25 26c0-6 3-9 8-9s8 3 8 9z" fill="#fff"/><path d="M10 34c0-10 5-15 11-15s11 5 11 15z" fill="#fff"/></svg>
    </div></div>
    <h3>Anyone can pay</h3>
    <p>Sed ut perspiciatis unde omnis iste natus error sit<br>totam rem aperiam, eaque ipsa quae ab illo.</p>
  </div>
</section>

<section class="info-band">
  <div class="tab active" style="top:29px">
    <svg width="18" height="18" viewBox="0 0 18 18"><circle cx="9" cy="9" r="6" fill="none" stroke="#222" stroke-width="3" stroke-dasharray="3 2"/><circle cx="9" cy="9" r="3" fill="none" stroke="#222" stroke-width="1.5"/></svg>How It Works</div>
  <div class="tab" style="top:76px">
    <svg width="16" height="16" viewBox="0 0 16 16"><circle cx="8" cy="4.5" r="3.5" fill="#fff"/><path d="M2 16c0-5 3-7 6-7s6 2 6 7z" fill="#fff"/></svg>Individuals</div>
  <div class="tab" style="top:122px">
    <svg width="18" height="16" viewBox="0 0 18 16"><rect x="1" y="4" width="16" height="11" rx="1.5" fill="#fff"/><rect x="6" y="1" width="6" height="4" fill="none" stroke="#fff" stroke-width="1.5"/><path d="M5 4v11M13 4v11" stroke="#1a5877" stroke-width="1.2"/></svg>Business</div>
  <div class="tab" style="top:169px">
    <svg width="18" height="17" viewBox="0 0 18 17"><path d="M9 0 18 4H0z" fill="#fff"/><rect x="0" y="4.5" width="18" height="1.5" fill="#fff"/><path d="M2 7h2v7H2zM6 7h2v7H6zM10 7h2v7h-2zM14 7h2v7h-2z" fill="#fff"/><rect x="0" y="15" width="18" height="2" fill="#fff"/></svg>Goverment</div>

  <div class="video-frame">
    <div class="video-still" role="img" aria-label="Video still: a businessman drawing money transfer routes across a world map">
      <span class="play"></span>
    </div>
  </div>

  <div class="info-copy">
    <p>Et harum quidem rerum facilis est et expedita distinctio. Nam libero tempore, cum soluta nobis est eligendi optio cumque nihil impedit quo minus id quod maxime placeat facere possimus, omnis voluptas assumenda est, omnis dolor repellendus.</p>
    <p>Temporibus autem quibusdam et aut officiis debitis aut rerum necessitatibus saepe eveniet ut et voluptates repudiandae sint et molestiae non recusandae.</p>
  </div>
  <div class="know-more">Know More
    <svg width="11" height="11" viewBox="0 0 11 11"><circle cx="5.5" cy="5.5" r="5.5" fill="#1d4e66"/><path d="M3 5.5h4.5M5.5 3.2 7.8 5.5 5.5 7.8" fill="none" stroke="#1b97c8" stroke-width="1.4"/></svg>
  </div>
</section>

<section class="partners">
  <span class="partner" style="left:92px"><i></i>Halvenmark</span>
  <span class="partner" style="left:196px"><i></i>Tollbrook</span>
  <span class="partner" style="left:300px">Vantori Telecard</span>
  <span class="partner" style="left:418px"><i></i>Plimsey Telecom</span>
  <span class="partner" style="left:528px">Orsel Dunn</span>
  <span class="partner" style="left:636px">Fenby Hollow</span>
</section>

<footer class="site-footer">
  <div class="footer-brand">Quarlen</div>
  <div class="legal">©2015Quarlen.All Rights Reserved<br>Privacy Policy</div>
  <span class="social" style="left:58px"></span>
  <span class="social" style="left:85px"></span>
  <span class="social" style="left:112px"></span>
  <span class="social" style="left:139px"></span>

  <h4 class="footer-heading" style="left:236px">Newsletter</h4>
  <div class="news-input">Email Address....</div>
  <div class="news-btn">Sign Up</div>

  <h4 class="footer-heading" style="left:426px">Latest News</h4>
  <div class="news-item" style="top:49px"><span class="date">27/05/2014</span><br>Aliquam dapibus tincidunt metus. Praesent quis, lobortis...&nbsp;&nbsp; <span class="meta">32 comments&nbsp;&nbsp; 2 Reviews</span></div>
  <div class="news-item" style="top:93px"><span class="date">27/05/2014</span><br>Aliquam dapibus tincidunt metus. Praesent quis, lobortis...&nbsp;&nbsp; <span class="meta">32 comments&nbsp;&nbsp; 2 Reviews</span></div>

  <h4 class="footer-heading" style="left:637px">How to Find Us</h4>
  <div class="find-us">8901 Street Name, City Name<br>Country Name.<br><br>Telephone:+1 012 345 6789<br>FAX:+ 1 123 456 7890<br>E-mail: <a>mail@quarlen.com</a></div>
</footer>

</body>
</html>
```